Marketing Skill "Workouts"; Design for an e-mail attachment highlighting Marketing training subjects

I am a freelance marketing trainer based in Singapore and need to e-mail out an attachment (probably saved as a PDF) to potential clients showing the training services I offer. These clients are all large blue-chip multinational companies so the attachment needs to look professional/high quality when opened on a computer.

My Company is called "Brightpath Marketing" (logo attached)

I am assuming the size should be A4 one sided colour.

I have attached some files that show best-attempts so far. These contain the key information, but the layouts all still look rather pedestrian. I am looking for something that looks a bit more dynamic but remains clear/easy to read.

Target Market(s)

HR/Marketing managers in multinational firms, mainly consumer goods

Industry/Entity Type

Marketing

Font styles to use
Sans Serif

Colors

Designer to choose colors to be used in the design.

Requirements
Must have
• Must look modern, up-to-date, professional.
Should not have
• Not gimmicky, like a cheap deal

```html
<!DOCTYPE html>
<html lang="en">
<head>
<meta charset="utf-8">
<title>Marketing Skill Workouts – Brightpath Marketing</title>
<link rel="stylesheet" href="https://fonts.googleapis.com/css2?family=Montserrat:wght@400;500;600;700;800&display=swap">
<style>
  :root {
    --hero-dark: #1c0608;
    --hero-mid: #4a1418;
    --hero-warm: #6b2226;
    --gold: #d9b45a;
    --white: #ffffff;
    --ink: #111111;
    --body-grey: #444444;
    --band-taupe: #7d716f;
    --band-light: #b9b5b6;
    --slate-top: #8e8e92;
    --slate-bottom: #65656a;
    --brand-red: #8e1a1f;
    --portrait-light: #c7c9cc;
    --portrait-dark: #6e7176;
  }
  * { margin: 0; padding: 0; box-sizing: border-box; }
  html, body { width: 960px; height: 1200px; overflow: hidden; background: var(--white); }
  body { font-family: "Montserrat", sans-serif; color: var(--ink); }
  .flyer { position: relative; width: 960px; height: 1200px; overflow: hidden; background: var(--white); }

  .hero-photo {
    position: absolute; left: 0; top: 0; width: 960px; height: 530px;
    background:
      radial-gradient(ellipse at 30% 45%, var(--hero-warm) 0%, var(--hero-mid) 35%, transparent 70%),
      linear-gradient(180deg, var(--hero-mid) 0%, var(--hero-dark) 100%);
  }
  .shape-layer { position: absolute; left: 0; top: 0; width: 960px; height: 1200px; }

  .hero-title {
    position: absolute; right: 70px; top: 68px; text-align: right;
    font-weight: 700; font-size: 56px; line-height: 66px; letter-spacing: 1px; color: var(--white);
  }
  .hero-title .accent { color: #d3d0d0; }
  .hook { position: absolute; left: 75px; top: 350px; color: var(--white); }
  .hook-question { font-weight: 700; font-size: 40px; color: var(--gold); letter-spacing: 1px; line-height: 46px; }
  .hook-answer { font-weight: 700; font-size: 24px; line-height: 30px; letter-spacing: 0.6px; margin-top: 4px; }

  .key-heading {
    position: absolute; left: 0; width: 960px; top: 482px; text-align: center;
    font-weight: 800; font-size: 60px; letter-spacing: 1px; line-height: 70px;
  }
  .column-divider { position: absolute; left: 479px; top: 548px; width: 2px; height: 196px; background: var(--ink); }
  .column-heading { position: absolute; top: 550px; font-weight: 700; font-size: 26px; letter-spacing: 0.5px; }
  .column-heading.topics { right: 493px; }
  .column-heading.benefits { left: 492px; }
  .topic-list, .benefit-list {
    position: absolute; top: 595px; list-style: none;
    font-size: 12px; line-height: 13.7px; color: var(--body-grey);
  }
  .topic-list { right: 497px; text-align: right; }
  .topic-list li::after { content: " •"; }
  .benefit-list { left: 496px; }
  .benefit-list li::before { content: "•"; display: inline-block; width: 12px; }

  .portrait-photo {
    position: absolute; left: 630px; top: 735px; width: 330px; height: 338px;
    border-radius: 150px 150px 0 0;
    background: radial-gradient(ellipse at 45% 40%, var(--portrait-light) 0%, var(--portrait-dark) 90%);
  }
  .why-me { position: absolute; right: 355px; top: 835px; text-align: right; color: var(--white); }
  .why-me-heading { font-weight: 800; font-size: 54px; line-height: 60px; letter-spacing: 1.5px; }
  .why-me-copy { font-size: 14.5px; line-height: 17.5px; margin-top: 8px; font-weight: 500; }
  .why-me-claim { font-size: 19px; font-weight: 500; margin-top: 12px; letter-spacing: 0.4px; }

  .brand-name {
    position: absolute; left: 58px; top: 1092px;
    font-weight: 500; font-size: 30px; line-height: 40px; color: var(--ink); letter-spacing: -0.3px;
  }
  .brand-dot {
    position: absolute; left: 392px; top: 1048px; width: 104px; height: 104px;
    border-radius: 50%; background: var(--brand-red); border: 8px solid var(--white);
  }
  .contact { position: absolute; left: 530px; top: 1088px; color: var(--ink); font-style: normal; }
  .contact-lead { font-weight: 700; font-size: 16px; line-height: 24px; }
  .contact-line { font-size: 22px; line-height: 28px; font-weight: 400; }
</style>
</head>
<body>
<main class="flyer">
  <div class="hero-photo" role="img" aria-label="Photograph of a woman training hard on gym equipment, tinted deep maroon"></div>

  <svg class="shape-layer" viewBox="0 0 960 1200" aria-hidden="true">
    <polygon points="0,508 480,458 960,508 960,530 0,530" fill="var(--band-taupe)"/>
    <polygon points="0,518 480,468 960,518 960,1200 0,1200" fill="var(--white)"/>
    <polygon points="0,810 480,757 960,810 960,1073 0,1073" fill="var(--band-light)"/>
    <defs>
      <linearGradient id="slate" x1="0" y1="0" x2="0" y2="1">
        <stop offset="0" stop-color="var(--slate-top)"/>
        <stop offset="1" stop-color="var(--slate-bottom)"/>
      </linearGradient>
    </defs>
    <polygon points="0,823 480,770 960,823 960,1073 0,1073" fill="url(#slate)"/>
  </svg>

  <h1 class="hero-title">Marketing Skill<br><span class="accent">“Workouts”</span></h1>
  <div class="hook">
    <p class="hook-question">No time to learn?</p>
    <p class="hook-answer">Problem solved with 1 day intensive workshops<br>that will drive business growth and motivate your team</p>
  </div>

  <h2 class="key-heading">KEY</h2>
  <div class="column-divider"></div>
  <h3 class="column-heading topics">TOPICS</h3>
  <h3 class="column-heading benefits">BENEFITS</h3>
  <ul class="topic-list">
    <li>Developing StrongBrand Plans</li>
    <li>Writing inspiring Briefs/Creative Evaluation</li>
    <li>Shopper Marketing/Developing Retail Promotions</li>
    <li>Brilliant Launch Management</li>
    <li>Improving Marketing R.O.I</li>
    <li>Driving Brand Growth without Product Innovation</li>
    <li>Insight/Concept Development</li>
    <li>Integrating Digital Channels</li>
    <li>Creativity and Idea Generation</li>
  </ul>
  <ul class="benefit-list">
    <li>Latest in world-class thinking/tools/case studies</li>
    <li>Ability to “customize” to address your specific business issues</li>
    <li>Take-away “checklists” to embed behaviors and skills</li>
    <li>Asian context / relevance</li>
    <li>Proven quality</li>
  </ul>

  <div class="portrait-photo" role="img" aria-label="Head-and-shoulders portrait photograph of the trainer in a dark suit"></div>

  <section class="why-me">
    <h2 class="why-me-heading">WHY ME?</h2>
    <p class="why-me-copy">The latest thinking, made practical and actionable.<br>20 years of business experience combined with over 10 years<br>of proven training/facilitation for major “blue-chip” clients,<br>regularly scoring 90%+ satisfaction</p>
    <p class="why-me-claim">World Class Quality without the costs</p>
  </section>

  <span class="brand-name">Brightpath Marketing</span>
  <span class="brand-dot" aria-hidden="true"></span>
  <address class="contact">
    <p class="contact-lead">Please get in touch;</p>
    <p class="contact-line">alex@brightpathmarketing.com</p>
    <p class="contact-line">+65 9100 4400</p>
  </address>
</main>
</body>
</html>
```